Need a sleek, professional business card design for a Web Development business

I need a unique business card designed for a web development company. It is also the parent company for any ventures I do, such as my ClipWave channel, startup ideas I have, etc. I am the single member of "Bright Harbor Code LLC." I will attach my basic logo here, so you will see the current color scheme and have the asset available. Thank you!

Target Market(s)

Startups, SMB's, Professionals

Industry/Entity Type

Business

Font styles to use
Other font styles liked:
• Lovello for headings is what I use, but not necessary.

Colors

Designer to choose colors to be used in the design.

Requirements
Nice to have
• Sleek is the word. Professional, modern, dark.
Should not have
• Any work from someone else's design. Lacking originality.

```html
<!DOCTYPE html>
<html lang="en">
<head>
<meta charset="utf-8">
<title>Bright Harbor Code LLC — Business Card</title>
<link rel="stylesheet" href="https://fonts.googleapis.com/css2?family=Ubuntu+Condensed&display=swap">
<style>
  :root {
    --page: #ffffff;
    --card-dark: #000000;
    --card-light: #ffffff;
    --ink-light: #ffffff;
    --ink-dark: #1c1c1c;
    --ink-muted: #8a8a8a;
    --icon-grey: #a3a3a5;
    --orange-start: #f7941d;
    --orange-end: #ef5a28;
    --rule: #5a5a5a;
    --ghost: #2a2a2a;
  }
  * { margin: 0; padding: 0; box-sizing: border-box; }
  html, body { width: 1200px; height: 1200px; overflow: hidden; background: var(--page); }
  body { position: relative; font-family: "Ubuntu Condensed", "Arial Narrow", sans-serif; }

  .card {
    position: absolute; left: 74px; top: 264px; width: 1064px; height: 595px;
    background: var(--card-light);
    box-shadow: 0 4px 18px rgba(0,0,0,0.35);
    overflow: hidden;
  }
  .card__dark { position: absolute; left: 0; top: 0; width: 100%; height: 464px; background: var(--card-dark); }
  .card__layer { position: absolute; left: 0; top: 0; width: 1064px; height: 595px; }

  .card__text { font-family: "Ubuntu Condensed", "Arial Narrow", sans-serif; }
  .brand-name { font-size: 41px; fill: var(--ink-light); }
  .brand-name .code { fill: var(--ink-muted); font-size: 32px; }
  .tagline { font-size: 22px; fill: var(--ink-light); }
  .tagline .soft { fill: var(--ink-muted); }
  .person-text { font-size: 29px; fill: var(--ink-light); }
  .person-text--name { font-size: 32px; }
  .contact { font-size: 28px; fill: var(--ink-dark); }

  .brand-mark {
    position: absolute; left: 36px; top: 151px; width: 149px; height: 150px;
    border: 2px solid var(--ink-light); border-radius: 7px;
    background: var(--card-dark);
  }
  .brand-mark--ghost {
    left: 652px; top: 153px; width: 148px; height: 148px;
    border-color: var(--ghost);
  }
</style>
</head>
<body>
<main class="card" aria-label="Business card for Bright Harbor Code LLC">
  <div class="card__dark"></div>

  <svg class="card__layer" viewBox="0 0 1064 595" aria-hidden="true">
    <defs>
      <linearGradient id="band-fill" x1="0" x2="1" y1="0" y2="0">
        <stop offset="0" stop-color="#f7941d"/>
        <stop offset="1" stop-color="#ef5a28"/>
      </linearGradient>
      <linearGradient id="brand-rule-fill" x1="0" x2="1" y1="0" y2="0">
        <stop offset="0" stop-color="#5a5a5a" stop-opacity="0"/>
        <stop offset="0.15" stop-color="#5a5a5a"/>
        <stop offset="0.85" stop-color="#5a5a5a"/>
        <stop offset="1" stop-color="#5a5a5a" stop-opacity="0"/>
      </linearGradient>
      <linearGradient id="address-rule-fill" x1="0" x2="1" y1="0" y2="0">
        <stop offset="0" stop-color="#ffffff" stop-opacity="0"/>
        <stop offset="0.4" stop-color="#ffffff"/>
      </linearGradient>
    </defs>
    <rect x="0" y="464" width="490" height="38" fill="url(#band-fill)"/>
    <rect x="580" y="464" width="484" height="38" fill="url(#band-fill)"/>
    <polygon points="478,462 532,430 532,477 490,502" fill="url(#band-fill)"/>
    <polygon points="532,430 592,462 582,502 532,477" fill="url(#band-fill)"/>

    <rect x="204" y="238" width="390" height="1" fill="url(#brand-rule-fill)"/>
    <rect x="846" y="164" width="168" height="1" fill="#ffffff"/>
    <rect x="838" y="327" width="176" height="1" fill="url(#address-rule-fill)"/>
  </svg>

  <div class="brand-mark" aria-hidden="true"></div>
  <div class="brand-mark brand-mark--ghost" aria-hidden="true"></div>

  <svg class="card__layer card__text" viewBox="0 0 1064 595">
    <text class="brand-name" x="202" y="224" textLength="396" lengthAdjust="spacingAndGlyphs"><tspan class="code">&lt;</tspan> Bright Harbor <tspan class="code">/&gt;</tspan> Code LLC</text>
    <text class="tagline" x="212" y="263" textLength="375" lengthAdjust="spacingAndGlyphs">Sleek is the word. Professional, modern, <tspan class="soft">dark.</tspan></text>

    <text class="person-text person-text--name" x="968" y="156" text-anchor="end">John DOE</text>
    <g fill="#ffffff">
      <circle cx="996" cy="138" r="9"/>
      <path d="M980 165 C980 152 987 148 996 148 C1005 148 1012 152 1012 165 Z"/>
    </g>
    <text class="person-text" x="1012" y="191" text-anchor="end">Web Developer</text>

    <text class="person-text" x="968" y="316" text-anchor="end">Address</text>
    <g transform="translate(975 289)">
      <path d="M19.5 2 L37 18 L33 18 L33 35 L6 35 L6 18 L2 18 Z" fill="none" stroke="#ffffff" stroke-width="3" stroke-linejoin="round"/>
      <rect x="27" y="4" width="4" height="8" fill="#ffffff"/>
      <rect x="16" y="22" width="8" height="13" fill="#ffffff"/>
    </g>
    <text class="person-text" x="1012" y="362" text-anchor="end">Steet</text>

    <g transform="translate(146 526)">
      <rect x="8" y="0" width="4" height="10" fill="#a3a3a5"/>
      <rect x="1" y="8" width="32" height="50" rx="7" fill="#a3a3a5"/>
      <rect x="6" y="14" width="22" height="17" rx="2" fill="#ffffff"/>
      <circle cx="21" cy="47" r="4" fill="#ffffff"/>
    </g>
    <text class="contact" x="191" y="562" textLength="113" lengthAdjust="spacingAndGlyphs">123456790</text>

    <g transform="translate(346 531)">
      <rect x="2.5" y="2.5" width="57" height="41" fill="none" stroke="#a3a3a5" stroke-width="5"/>
      <path d="M3 4 L31 24 L59 4" fill="none" stroke="#a3a3a5" stroke-width="5"/>
    </g>
    <text class="contact" x="424" y="562" textLength="209" lengthAdjust="spacingAndGlyphs">info@example.com</text>

    <g transform="translate(658 525)">
      <g fill="none" stroke="#a3a3a5" stroke-width="4">
        <circle cx="26" cy="26" r="23"/>
        <ellipse cx="26" cy="26" rx="10" ry="23"/>
        <line x1="3" y1="26" x2="49" y2="26"/>
        <line x1="26" y1="3" x2="26" y2="49"/>
      </g>
      <path d="M32 28 L54 42 L44 44 L50 55 L45 57 L39 46 L32 52 Z" fill="#a3a3a5" stroke="#ffffff" stroke-width="2"/>
    </g>
    <text class="contact" x="726" y="562" textLength="200" lengthAdjust="spacingAndGlyphs">www.example.com</text>
  </svg>
</main>
</body>
</html>
```